KEEP YOUR HARBOR

Our business will reach out to business owners and offer a variety of services, predominantly the following: a) a free review of the owner's business structure to make sure it was properly formed, b) litigation representation at an extremely discounted rate (we plan to engage in direct marketing to civil litigation defendants, c) weekly "attorney letters" at no charge, d) free legal forms that are commonly used in business, and e) by far, the most important service offered is the licensed use of a copyrighted clause that is incorporated into virtually any commercial agreement (hereafter referred to as "the Clause").
The effect of the Clause is to require that parties to a contract ("Contract") notify each other, in writing, of any fact or event (referred to as "Event") that might impact the Contract. And the failure to comply with the Clause results in the non-complying party being given a significant advantage should the Contract become the subject of a lawsuit, in particular, an advantage over issues commonly referred to "he said / she said" issues. We believe that most civil litigation hinges on at least one or more of such issues, i.e., issues for which there is no concrete proof one way or the other. In such cases, the party taking advantage of the Clause will very likely prevail on all such issues -- in other words, using the Clause will likely prevent litigation from being pursued against such party, or likely result in such party prevailing in court. ARE ALL THESE SERVICES WORTH $9.95 PER WEEK?

Target Market(s)

#1. Current defendants in civil litigation cases, #2 business owners who get sued by: a) employees, b) business associates, who believe they have claims against the owner or the business.

Industry/Entity Type

Legal claims are increasing in large part because of the leverage that exists in forcing businesses to hire legal counsel to defend "he said / she said" claims -

Number of Pages Required

1 page

Colors
0094D4
00A9DD
6FCCEA
C7EBF8
E9F6FB

Requirements
Must have
• Professional appearance. We are explaining that there are wolves out there in the form of employees and business associates who can turn into enemies by making groundless allegations that could easily cost tens of thousands of dollars -- and it does more frequently than you might think.
Nice to have
• I like to refer to Amos Whitcombe's classic axiom: an ounce of prevention is worth a pound of cure -- with anecdotes taken from actual examples of why the services offered, i.e., the extreme discount of legal fees in the event of a lawsuit, being able to send attorney letters sent out every week at no charge, and above all, the right to incorporate copyrighted contractual provisions that make it very difficult for employees and business associates to make claims against you that evolve into lawsuits -- are each worth far more than the paltry membership fee of $9.95 per week.

```html
<!DOCTYPE html>
<html lang="en">
<head>
<meta charset="utf-8">
<title>Keepyourharbor.Net</title>
<link href="https://fonts.googleapis.com/css2?family=Arimo:wght@400;600;700&family=Raleway:wght@400;500;600&display=swap" rel="stylesheet">
<style>
:root{
  --teal:#137f8c;
  --teal-light:#2aa5b4;
  --ink:#1c1f22;
  --text:#3c4146;
  --paper:#ffffff;
  --mist:#f2f3f4;
  --field-text:#8a8f94;
}
*{margin:0;padding:0;box-sizing:border-box}
html,body{width:1200px;height:3723px;overflow:hidden}
body{position:relative;background:var(--paper);font-family:"Raleway",sans-serif;color:var(--text)}
.abs{position:absolute}
.heading{font-family:"Arimo",sans-serif;font-weight:700;color:var(--ink)}
.btn{position:absolute;display:flex;align-items:center;justify-content:center;background:var(--teal);color:#fff;font-family:"Arimo",sans-serif;font-weight:700;font-size:15px;border-radius:4px;letter-spacing:.2px}
.btn-light{background:#fff;color:var(--teal)}
.underline{position:absolute;height:3px;width:38px;background:var(--teal);left:581px}
.section-title{position:absolute;left:0;width:1200px;text-align:center;font-size:30px}
.bar{position:absolute;width:4px;background:var(--teal)}

/* bands */
.hero-band{left:0;top:0;width:1200px;height:600px;background:linear-gradient(100deg,#2f2f2f 0%,#555 45%,#4a4a4a 100%)}
.hero-panel{left:652px;top:98px;width:548px;height:502px;background:linear-gradient(160deg,#ffffff 0%,#f3f3f3 60%,#dcdcdc 100%)}
.services-band{left:0;top:1031px;width:1200px;height:571px;background:var(--mist)}
.breach-band{left:0;top:2201px;width:1200px;height:525px;background:linear-gradient(180deg,#177f8c 0%,#137a86 70%,#157481 100%)}
.footer-band{left:0;top:3308px;width:1200px;height:415px;background:linear-gradient(180deg,#1a1f22,#20272b)}

/* nav */
.brand{position:absolute;font-family:"Arimo",sans-serif;font-weight:700;color:#fff;font-size:29px;line-height:34px}
.nav-link{position:absolute;top:38px;color:#fff;font-family:"Arimo",sans-serif;font-size:15px;line-height:18px;text-decoration:none;font-weight:600}
.nav-link.is-active{color:var(--teal-light)}
.nav-phone{position:absolute;top:38px;left:849px;color:#fff;font-size:16px;line-height:18px;font-weight:500}

/* hero */
.hero-title{position:absolute;left:112px;top:240px;font-family:"Arimo",sans-serif;color:#fff;font-size:26px;line-height:44px;font-weight:700}
.hero-title span{color:var(--teal)}
.hero-text{position:absolute;left:112px;top:340px;width:470px;color:#f0f0f0;font-size:15px;line-height:25px}

/* about */
.about-text{position:absolute;left:150px;top:744px;width:900px;text-align:center;font-size:15px;line-height:25.7px;color:var(--text)}

/* services */
.card{position:absolute;top:1186px;width:233px;height:344px;background:#fff;border-radius:4px;box-shadow:0 4px 14px rgba(0,0,0,.07);overflow:hidden}
.card-pic{height:172px}
.card-label{position:absolute;top:190px;left:12px;right:12px;height:100px;display:flex;align-items:center;justify-content:center;text-align:center;font-family:"Arimo",sans-serif;font-weight:700;font-size:14.5px;line-height:25.5px;color:var(--ink)}
.card-more{position:absolute;top:301px;left:0;right:0;text-align:center;font-family:"Arimo",sans-serif;font-weight:700;font-size:14.5px;color:var(--teal)}
.card.is-active{background:var(--teal)}
.card.is-active .card-label,.card.is-active .card-more{color:#fff}
.arrow{position:absolute;width:46px;height:46px;border-radius:50%;display:flex;align-items:center;justify-content:center}

/* feature blocks */
.feature-title{position:absolute;font-size:30px;line-height:47px}
.feature-text{position:absolute;width:430px;font-size:15px;line-height:25.6px;text-align:justify}

/* faq */
.faq-item{position:absolute;left:272px;width:655px;background:#fff;border:1px solid #e8e9ea;border-radius:4px;box-shadow:0 3px 10px rgba(0,0,0,.06)}
.faq-q{position:absolute;left:37px;top:21px;font-family:"Arimo",sans-serif;font-weight:700;font-size:21px;color:var(--ink)}
.faq-item.is-open .faq-q{color:var(--teal)}
.faq-a{position:absolute;left:36px;top:72px;width:520px;font-size:14.5px;line-height:25.5px}
.toggle{position:absolute;right:18px;top:20px;width:33px;height:29px;background:var(--teal);border-radius:3px;display:flex;align-items:center;justify-content:center}

/* footer */
.footer-heading{position:absolute;font-family:"Arimo",sans-serif;font-weight:700;font-size:19px;color:#fff}
.footer-list{position:absolute;list-style:none;font-size:15px;line-height:26px;color:#fff}
.field{position:absolute;width:236px;height:48px;background:#fff;border-radius:4px;font-size:14px;color:var(--field-text);padding:15px 14px}
.send{position:absolute;left:603px;top:3564px;width:483px;height:51px;background:var(--teal);border-radius:4px;color:#fff;font-size:15px;padding:16px 14px}
.copyright{position:absolute;left:0;top:3678px;width:1200px;text-align:center;font-size:15px;color:#e7e9ea}
</style>
</head>
<body>

<!-- Hero -->
<div class="abs hero-band" role="img" aria-label="Background photo of a hand signing a document with a pen"></div>
<div class="abs hero-panel" role="img" aria-label="Ink illustration of Amos Whitcombe writing with a quill pen by candlelight"></div>

<header>
  <div class="brand" style="left:111px;top:30px">Keepyourharbor.Net</div>
  <a class="nav-link is-active" style="left:453px" href="#">Home</a>
  <a class="nav-link" style="left:531px" href="#">Services</a>
  <a class="nav-link" style="left:626px" href="#">Faq</a>
  <a class="nav-link" style="left:687px" href="#">Contact Us</a>
  <span class="abs" style="left:795px;top:37px;color:#fff;font-size:15px">|</span>
  <svg class="abs" style="left:822px;top:39px" width="17" height="17" viewBox="0 0 24 24"><path fill="#fff" d="M6.6 10.8a15.1 15.1 0 0 0 6.6 6.6l2.2-2.2c.3-.3.7-.4 1-.2 1.1.4 2.3.6 3.6.6.6 0 1 .4 1 1V20c0 .6-.4 1-1 1C10.6 21 3 13.4 3 4c0-.6.4-1 1-1h3.5c.6 0 1 .4 1 1 0 1.3.2 2.5.6 3.6.1.3 0 .7-.2 1z"/></svg>
  <span class="nav-phone">(555) 014-2290</span>
  <div class="btn" style="left:995px;top:29px;width:93px;height:39px">LOG IN</div>
</header>

<h1 class="hero-title">ARE ALL THESE SERVICES WORTH<br><span>$9.95 PER WEEK?</span></h1>
<p class="hero-text">KEEP YOUR HARBOR (“KYH”) is a referral service that helps the business owner avoid LEGAL CONFLICT</p>
<div class="btn" style="left:113px;top:418px;width:290px;height:45px">WHAT A MEMBERSHIP INCLUDES</div>

<!-- About -->
<div class="abs" style="left:1040px;top:660px;width:160px;height:215px;background:linear-gradient(160deg,#fafafa,#f1f1f1)" role="img" aria-label="Faint line drawing of two pens"></div>
<h2 class="heading section-title" style="top:678px">About Us</h2>
<p class="about-text">KEEP YOUR HARBOR (“KYH”) is a referral service that helps the business owner avoid LEGAL CONFLICT by referring attorneys who offer services uniquely designed to minimize – if not altogether eliminate – those conflicts that can and do evolve into COSTLY LITIGATION. And by “costly,” we mean that, in today’s world, the costs of civil litigation have skyrocketed out of control, to the point that, in far too many cases, civil litigation is simply not affordable, giving those with superior economic means a disproportionately UNFAIR ADVANTAGE in the dispute resolution process. A membership in KYH levels the playing field.</p>
<div class="btn" style="left:532px;top:901px;width:136px;height:45px">LEARN MORE</div>

<!-- Services -->
<div class="abs services-band"></div>
<h2 class="heading section-title" style="top:1097px">Our Services</h2>
<div class="underline" style="top:1137px"></div>

<div class="arrow" style="left:44px;top:1333px;background:var(--teal)">
  <svg width="22" height="22" viewBox="0 0 24 24"><path d="M20 12H5M11 6l-6 6 6 6" stroke="#fff" stroke-width="2.4" fill="none" stroke-linecap="round" stroke-linejoin="round"/></svg>
</div>
<div class="arrow" style="left:1111px;top:1333px;background:#fff;box-shadow:0 2px 8px rgba(0,0,0,.08)">
  <svg width="22" height="22" viewBox="0 0 24 24"><path d="M4 12h15M13 6l6 6-6 6" stroke="#137f8c" stroke-width="2.4" fill="none" stroke-linecap="round" stroke-linejoin="round"/></svg>
</div>

<article class="card" style="left:111px">
  <div class="card-pic" role="img" aria-label="Photo of business people meeting in an office" style="background:linear-gradient(135deg,#8b9095,#c9ccce 50%,#4b4f54)"></div>
  <div class="card-label">A Free Review Of The Owner's Business Structure To Make Sure It Was Properly Formed</div>
  <div class="card-more">Learn More →</div>
</article>
<article class="card is-active" style="left:360px">
  <div class="card-pic" role="img" aria-label="Photo of a document being signed beside cash" style="background:linear-gradient(135deg,#e6e6e4,#9d9d99 55%,#2d2d2d)"></div>
  <div class="card-label">litigation representation at an extremely discounted rate</div>
  <div class="card-more">Learn More →</div>
</article>
<article class="card" style="left:607px">
  <div class="card-pic" role="img" aria-label="Photo of a stamp and fountain pen on paper" style="background:linear-gradient(135deg,#6d4a33,#b89c84 45%,#ece7e1)"></div>
  <div class="card-label">weekly "attorney letters" at no charge</div>
  <div class="card-more">Learn More →</div>
</article>
<article class="card" style="left:856px">
  <div class="card-pic" role="img" aria-label="Photo of a businessman reviewing forms at a laptop" style="background:linear-gradient(135deg,#2c3440,#6b7480 50%,#d7d9dc)"></div>
  <div class="card-label">free legal forms that are commonly used in business</div>
  <div class="card-more">Learn More →</div>
</article>

<!-- Litigation -->
<div class="abs" style="left:0;top:1689px;width:600px;height:425px;background:linear-gradient(120deg,#cfc7bc 0%,#e7e2db 40%,#9a9289 75%,#3d3a37 100%)" role="img" aria-label="Photo of a lawyer presenting documents to colleagues in a law library"></div>
<div class="bar" style="left:636px;top:1722px;height:73px"></div>
<h2 class="heading feature-title" style="left:658px;top:1712px;color:#1f2528">Civil Litigation Defense @<br>Discounted Rates</h2>
<p class="feature-text" style="left:659px;top:1824px">If you have been sued, you may have no choice but to hire an attorney or law firm to represent you, if you are, for example, a legal entity like a corporation or limited liability company. The costs of hiring an attorney to represent you can easily run in the $25,000 to $50,000 range.Unfortunately, initial retainers charged by many attorneys (typically $2,500 to $5,000) burn faster than a dry X’mas tree on fire.</p>
<div class="btn" style="left:659px;top:2034px;width:137px;height:44px">LEARN MORE</div>

<!-- Breach -->
<div class="abs breach-band"></div>
<div class="bar" style="left:88px;top:2282px;height:75px;background:#fff"></div>
<h2 class="heading feature-title" style="left:112px;top:2270px;color:#fff">Notification Of Possible Breach<br>Re: Contracts</h2>
<p class="feature-text" style="left:113px;top:2382px;width:490px;color:#eaf6f7">Very likely, the most important feature of our membership is the right to require that parties to your contractual relationships notify you of events that might be considered BREACHES of those relationships. The purpose of this requirement is to ensure that you be notified of potential issues so they can be identified and defined. The importance of being notified is to give you the opportunity to address and hopefully resolve these issues.</p>
<div class="btn btn-light" style="left:113px;top:2593px;width:137px;height:44px">LEARN MORE</div>
<svg class="abs" style="left:704px;top:2268px" width="388" height="388" viewBox="0 0 388 388">
  <circle cx="194" cy="194" r="192" fill="none" stroke="#fff" stroke-width="2"/>
</svg>
<div class="abs" style="left:714px;top:2274px;width:372px;height:372px;border-radius:50%;background:linear-gradient(135deg,#e9ecef 0%,#b9c0c6 45%,#2b3036 80%)" role="img" aria-label="Photo of two businessmen handing over a contract"></div>

<!-- FAQ -->
<div class="abs" style="left:0;top:2740px;width:250px;height:520px;background:radial-gradient(ellipse at 30% 50%,#eceeef 0%,rgba(255,255,255,0) 70%)" role="img" aria-label="Faint engraved portrait decoration"></div>
<div class="abs" style="left:1090px;top:2790px;width:110px;height:340px;background:radial-gradient(ellipse at 60% 50%,#eeeff0 0%,rgba(255,255,255,0) 70%)" role="img" aria-label="Faint quill feather decoration"></div>
<h2 class="heading section-title" style="top:2808px">Frequently Asked Questions</h2>
<div class="underline" style="top:2850px"></div>

<div class="faq-item" style="top:2903px;height:68px">
  <h3 class="faq-q">Customer Question #1</h3>
  <div class="toggle"><svg width="14" height="14" viewBox="0 0 24 24"><path d="M6 9l6 6 6-6" stroke="#fff" stroke-width="3" fill="none"/></svg></div>
</div>
<div class="faq-item is-open" style="top:2994px;height:138px">
  <h3 class="faq-q">Customer Question #2</h3>
  <div class="toggle"><svg width="14" height="14" viewBox="0 0 24 24"><path d="M6 15l6-6 6 6" stroke="#fff" stroke-width="3" fill="none"/></svg></div>
  <p class="faq-a">This is your Answer section. Use it to answer a common question and to showcase a unique element of your business.</p>
</div>
<div class="faq-item" style="top:3153px;height:70px">
  <h3 class="faq-q">Customer Question #3</h3>
  <div class="toggle"><svg width="14" height="14" viewBox="0 0 24 24"><path d="M6 9l6 6 6-6" stroke="#fff" stroke-width="3" fill="none"/></svg></div>
</div>

<!-- Footer -->
<div class="abs footer-band"></div>
<div class="brand" style="left:111px;top:3413px">Keepyourharbor.Net</div>
<h4 class="footer-heading" style="left:112px;top:3481px">Quick links</h4>
<ul class="footer-list" style="left:112px;top:3516px"><li>Home</li><li>Services</li><li>Faq</li><li>Contact Us</li></ul>
<h4 class="footer-heading" style="left:333px;top:3482px">Hours</h4>
<ul class="footer-list" style="left:333px;top:3516px"><li>Monday to Friday</li><li>9:00 a.m - 05:00 p.m.</li><li>Saturday &amp; Sunday</li><li>Closed</li></ul>
<h4 class="footer-heading" style="left:606px;top:3384px;font-size:28px">Contact us</h4>
<div class="field" style="left:603px;top:3437px">First Name</div>
<div class="field" style="left:850px;top:3437px">Last Name</div>
<div class="field" style="left:603px;top:3499px">Phone</div>
<div class="field" style="left:850px;top:3499px">Email</div>
<div class="send">Send Message
  <svg class="abs" style="right:26px;top:18px" width="17" height="14" viewBox="0 0 24 20"><path fill="#fff" d="M2 2h20v16H2z"/><path d="M2 2l10 8 10-8" stroke="#137f8c" stroke-width="2" fill="none"/></svg>
</div>
<div class="copyright">©Copyrights 2022 Keepyourharbor &nbsp;| &nbsp; All Rights Reserved</div>

</body>
</html>
```